Startup Biz for Seniors needs your help!

Our business is a Startup that Employs Caregivers to do IN HOME Care of the Elderly. Our website is not yet running. But, a business similar to ours is Tallbrookcare.com

We are looking for a card that only has 4 Elements:
-Logo
- Website
- Tag Line
- Phone
We would like to see some eye catching backgrounds.
We would like to see some designs with and some without a Photo.
Would like the Photo to be of a Caregiver taking care of a Senior. The photo should show both of them smiling.

Target Market(s)

Age 35-55 who has Parents that are Elderly and need care

Industry/Entity Type

Home Health Care

Contact Information for Business Card

Want it to Pop Out to the viewer . Thinking maybe:
Side 1: LOGO with Website & Tag line
Side 2: Phone Number

Font styles to use
Other font styles liked:
• Same Font as our Logo

Colors

Designer to choose colors to be used in the design.

Requirements
Must have
• Logo, website, Tag Line, Phone number and Email: "info@velvetdays.example"
• Please use one of the photos that I have attached.
Nice to have
• Would like to see a Photo worked in that has a Care Taker taking care of an Elderly Person and they are both smiling.

```html
<!DOCTYPE html>
<html lang="en">
<head>
<meta charset="utf-8">
<title>VelvetDays Business Card</title>
<link rel="stylesheet" href="https://fonts.googleapis.com/css2?family=Fredoka:wght@600&family=Lobster+Two:ital,wght@1,700&family=Spline+Sans+Mono:wght@300&family=Poppins:wght@400&display=swap">
<style>
  :root {
    --canvas: #ffffff;
    --card-dark: #000000;
    --brand-blue: #2f63b3;
    --brand-orange: #ef5a2a;
    --ink: #1d1d1d;
    --photo-light: #e8eaec;
    --photo-mid: #c9d0d8;
    --photo-blue: #9fb6d3;
  }
  * { margin: 0; padding: 0; box-sizing: border-box; }
  html, body {
    width: 1200px;
    height: 1200px;
    overflow: hidden;
    background: var(--canvas);
  }
  .stage { position: relative; width: 1200px; height: 1200px; }

  .card { position: absolute; overflow: hidden; }

  .card-front {
    left: 316px; top: 254px;
    width: 451px; height: 276px;
    background: var(--card-dark);
  }
  .card-back {
    left: 386px; top: 618px;
    width: 450px; height: 275px;
  }

  .brand-mark {
    position: absolute;
    border-radius: 50%;
    background: var(--brand-orange);
  }
  .brand-name {
    position: absolute;
    font-family: "Fredoka", sans-serif;
    font-weight: 600;
    color: var(--brand-blue);
    white-space: nowrap;
    line-height: 1;
  }
  .tagline {
    position: absolute;
    font-family: "Lobster Two", cursive;
    font-style: italic;
    font-weight: 700;
    color: var(--brand-blue);
    white-space: nowrap;
    line-height: 1;
  }

  .card-front .brand-mark { left: 84px; top: 106px; width: 66px; height: 66px; }
  .card-front .brand-name { left: 154px; top: 120px; font-size: 22px; }
  .card-front .tagline   { left: 178px; top: 145px; font-size: 15px; }

  .photo-area {
    position: absolute; inset: 0;
    background:
      radial-gradient(ellipse at 55% 80%, var(--photo-blue) 0%, transparent 55%),
      linear-gradient(120deg, var(--photo-mid) 0%, var(--photo-light) 55%, #f1f2f3 100%);
  }
  .card-back .brand-mark { left: 194px; top: 8px; width: 50px; height: 50px; }
  .card-back .brand-name { left: 242px; top: 18px; font-size: 27px; }

  .phone {
    position: absolute;
    left: 238px; top: 218px;
    font-family: "Spline Sans Mono", monospace;
    font-weight: 300;
    font-size: 20px;
    letter-spacing: 2px;
    color: var(--ink);
    white-space: nowrap;
  }
  .website {
    position: absolute;
    left: 239px; top: 244px;
    font-family: "Poppins", sans-serif;
    font-size: 8px;
    letter-spacing: 4.2px;
    color: var(--ink);
    white-space: nowrap;
  }
</style>
</head>
<body>
<main class="stage">
  <section class="card card-front" aria-label="Business card front">
    <span class="brand-mark" aria-hidden="true"></span>
    <span class="brand-name">VelvetDays.example</span>
    <span class="tagline">Senior Care - Family Style</span>
  </section>

  <section class="card card-back" aria-label="Business card back">
    <div class="photo-area" role="img" aria-label="Faded photo of a smiling caregiver with her arms around a smiling elderly woman"></div>
    <span class="brand-mark" aria-hidden="true"></span>
    <span class="brand-name">VelvetDays</span>
    <span class="phone">+672-555-0148</span>
    <span class="website">www.velvetdays.example</span>
  </section>
</main>
</body>
</html>
```